Hand made soap for men packaging design

Need packaging concept and mock-up for new product line of handmade bar soaps for men. Please read the attached project brief for packaging requirements and examples. Adobe Illustrator logo files are attached as well.

Our company, Steel And Stone Co.™, specializes in high-end self-care products for men. We focus on the needs of high-performing men in their mid-30’s to 50’s who have worked hard to achieve their goals. We encourage a strong, positive view of masculinity where traits such as courage, bravery, competition, stoicism, toughness, and independence are celebrated.

Our body and skincare products use natural and organic ingredients that are designed to inspire confidence in everything men do, with a distinct focus on anti-aging benefits and enhancement to overall male virility and health. We avoid estrogenics and other ingredients that have been shown to have adverse effects on men’s health, most notably the production of testosterone.

Quartet™ is our initial product line consisting of all-natural handmade soaps that make up a basic daily skin care routine for men in our target niche. This product line is inspired by the Greek philosopher, Aristotle, who was the first to theorize about the four (4) natural elements: Fire, Water, Air and Earth. There are four (4) individual soap variations, each one associated with one of these elements. The alignment of the Quartet™ collection to Ancient Greece perfectly embodies the idea of manhood we promote at Steel And Stone Co.™, with this classical conception of masculinity defining manhood in the West up until the middle of the 20th century.

In addition to Quartet™ there will be additional collections released in the future, each one with it’s own concept, theme and design considerations.

Target Market(s)

Industry/Entity Type

Men's health, body/skin care products

Font styles to use
Sans Serif
Decorative
Other font styles liked:
• Any masculine font that aligns to theme of Ancient Greece

Requirements
Must have
• Project requirements are detailed in the attached MS Word project brief. Please design for one (1) product, but consider that there will be three (3) others designed later to complete the collection. Each product will carry the same general design theme created here.
Nice to have
• This product line is inspired by the Greek philosopher, Aristotle, who was the first to theorize about the four (4) natural elements: Fire, Water, Air and Earth. There are four (4) individual soap variations, each one associated with one of these elements. The alignment of the Quartet™ collection to Ancient Greece perfectly embodies the idea of manhood we promote at Steel And Stone Co.™, with this classical conception of masculinity defining manhood in the West up until the middle of the 20th century. Sample packaging concepts are included in the attached MS Word project brief.

```html
<!DOCTYPE html>
<html lang="en">
<head>
<meta charset="utf-8">
<title>Quartet Fire – Soap Box Front</title>
<link rel="stylesheet" href="https://fonts.googleapis.com/css2?family=Cinzel:wght@400;500;600&family=Oswald:wght@700&family=Josefin+Sans:wght@600&display=swap">
<style>
  :root {
    --page: #f4f2f0;
    --wine-deep: #2e070a;
    --wine: #4c080c;
    --wine-bright: #5e0a0e;
    --ember: #f29103;
    --cream: #f6ead8;
    --motif: rgba(120, 40, 40, 0.35);
  }
  * { margin: 0; padding: 0; box-sizing: border-box; }
  html, body {
    width: 1200px; height: 685px; overflow: hidden;
    background: var(--page);
  }
  .box-front {
    position: absolute; left: 290px; top: 42px;
    width: 620px; height: 600px; overflow: hidden;
    background: linear-gradient(160deg, var(--wine-deep) 0%, var(--wine) 45%, var(--wine-bright) 100%);
    color: var(--cream);
  }
  .art { position: absolute; inset: 0; }
  .brand {
    position: absolute; left: 190px; top: 52px;
    display: flex; align-items: center; gap: 16px;
  }
  .brand-dot {
    width: 58px; height: 58px; border-radius: 50%;
    border: 3px solid var(--cream); flex: none;
  }
  .brand-name {
    font-family: "Oswald", sans-serif; font-weight: 700;
    font-size: 38px; line-height: 1; letter-spacing: 0.5px;
    text-transform: uppercase; color: var(--cream);
    white-space: nowrap;
  }
  .brand-tagline {
    font-family: "Josefin Sans", sans-serif; font-weight: 600;
    font-size: 15px; letter-spacing: 2.4px; margin-top: 6px;
    text-transform: uppercase; color: var(--cream);
    white-space: nowrap;
  }
  .product-title {
    position: absolute; left: 318px; top: 250px;
    font-family: "Cinzel", serif; text-transform: uppercase;
    font-weight: 400;
  }
  .line-name { font-size: 38px; letter-spacing: 3px; color: var(--cream); line-height: 1.1; }
  .line-name sup { font-size: 14px; }
  .variant { font-size: 98px; line-height: 0.9; letter-spacing: 2px; color: var(--ember); font-weight: 600; }
  .notes {
    position: absolute; left: 0; right: 0; bottom: 50px; text-align: center;
    font-family: "Cinzel", serif; text-transform: uppercase;
  }
  .ingredients { font-size: 15px; color: var(--ember); letter-spacing: 1px; }
  .description { font-size: 15px; color: var(--cream); letter-spacing: 1px; margin-top: 6px; }
</style>
</head>
<body>
  <main class="box-front">
    <svg class="art" width="620" height="600" viewBox="0 0 620 600">
      <circle role="img" aria-label="Faint Greek key border ring" cx="0" cy="300" r="210" fill="none" stroke="var(--motif)" stroke-width="58"/>
      <path class="fire-sun" d="M0 160 A140 140 0 0 1 0 440 Z" fill="var(--ember)" transform="translate(12 0)"/>
      <polygon class="fire-triangle" points="440,150 590,430 290,430" fill="none" stroke="var(--motif)" stroke-width="16" stroke-linejoin="round"/>
    </svg>

    <header class="brand">
      <span class="brand-dot"></span>
      <div>
        <div class="brand-name">Steel And Stone Co.</div>
        <div class="brand-tagline">Built for every battle</div>
      </div>
    </header>

    <h1 class="product-title">
      <div class="line-name">Quartet<sup>TM</sup></div>
      <div class="variant">Fire</div>
    </h1>

    <section class="notes">
      <p class="ingredients">Cinnamon &bull; Clove &bull; Orange and Cade</p>
      <p class="description">Make for a spicy mysterious blend with a touch of smoke.</p>
    </section>
  </main>
</body>
</html>
```